依頼概要
■依頼の目的/概要
当方、眼鏡店です。7年以上ご来店が無い75歳以上の顧客様に、来店を促すDMを考えております。

■依頼詳細
枚数:約250枚
サイズ:はがきサイズ

■要望
・眼鏡店だとわかりやすいイラストをお願いします。
・添付ファイルの文面を入れて下さい。

その他何かご不明な点がございましたら、お気軽にご質問下さい。
よろしくお願いいたします。

・親しみやすいデザイン。
・サービス内容が分かりやすく書かれていた。

皆様からご提案頂き、誠にありがとうございました。
どれも素晴らしいデザイン案でしたので、選考にも大変悩みました。
また依頼させて頂いた際には、よろしくお願いいたします。

```html
<!DOCTYPE html>
<html lang="ja">
<head>
<meta charset="utf-8">
<title>老眼鏡 見直しのご案内</title>
<link rel="stylesheet" href="https://fonts.googleapis.com/css2?family=Noto+Sans+JP:wght@400;700;900&family=Noto+Serif+JP:wght@700;900&display=swap">
<style>
  :root {
    --green: #1f9a4a;
    --blue: #1a8fd0;
    --blue-deep: #1667a8;
    --orange: #f07a12;
    --red: #d8281e;
    --ink: #222222;
    --paper: #ffffff;
    --photo-light: #eeeeee;
    --photo-mid: #b9b9b9;
    --photo-dark: #6f6f6f;
  }
  html, body {
    margin: 0;
    padding: 0;
    width: 810px;
    height: 1200px;
    overflow: hidden;
    background: var(--paper);
  }
  .card {
    position: relative;
    width: 810px;
    height: 1200px;
    background: var(--paper);
    font-family: "Noto Sans JP", sans-serif;
    color: var(--ink);
    overflow: hidden;
    box-sizing: border-box;
    border: 2px solid #d0d0d0;
  }
  .photo-top {
    position: absolute;
    left: 0; top: 0;
    width: 100%; height: 480px;
    background: linear-gradient(160deg, var(--photo-light) 0%, var(--photo-mid) 45%, var(--photo-dark) 100%);
  }
  .headline {
    position: absolute;
    left: 237px; top: 0;
    width: 336px; height: 336px;
    border-radius: 50%;
    background: var(--green);
    display: flex;
    align-items: center;
    justify-content: center;
    text-align: center;
    color: #fff;
    font-weight: 900;
    font-size: 52px;
    line-height: 1.3;
    letter-spacing: 2px;
    padding-top: 10px;
    box-sizing: border-box;
  }
  .question-band {
    position: absolute;
    left: 0; top: 480px;
    width: 100%; height: 60px;
    background: var(--paper);
    display: flex;
    align-items: center;
    justify-content: center;
    font-family: "Noto Serif JP", serif;
    font-weight: 900;
    font-size: 31px;
    color: var(--blue-deep);
    letter-spacing: 1px;
  }
  .photo-bottom {
    position: absolute;
    left: 0; top: 540px;
    width: 100%; height: 458px;
    background: linear-gradient(200deg, var(--photo-light) 0%, #d4d4d4 50%, var(--photo-mid) 100%);
  }
  .couple-photo {
    position: absolute;
    left: 50px; top: 780px;
    width: 300px; height: 218px;
    background: linear-gradient(180deg, #e6dccd 0%, #c9b8a2 60%, #8a7b6c 100%);
  }
  .message {
    position: absolute;
    left: 210px; top: 570px;
    width: 390px; height: 390px;
    border-radius: 50%;
    background: rgba(26, 143, 208, 0.88);
    color: #fff;
    font-size: 23px;
    font-weight: 700;
    line-height: 1.55;
    display: flex;
    align-items: center;
    justify-content: center;
    text-align: left;
    padding: 0 54px;
    box-sizing: border-box;
  }
  .free-badge {
    position: absolute;
    left: 566px; top: 756px;
    width: 208px; height: 208px;
    border-radius: 50%;
    background: var(--orange);
    color: #fff;
    text-align: center;
    display: flex;
    flex-direction: column;
    align-items: center;
    justify-content: center;
  }
  .free-badge .service {
    background: #fff;
    color: var(--red);
    font-weight: 700;
    font-size: 19px;
    line-height: 1.25;
    padding: 4px 10px;
  }
  .free-badge .free {
    font-weight: 900;
    font-size: 50px;
    line-height: 1.15;
    letter-spacing: 2px;
  }
  .free-badge .note {
    font-size: 12px;
    line-height: 1.35;
  }
  .welcome-band {
    position: absolute;
    left: 0; top: 998px;
    width: 100%; height: 48px;
    background: var(--blue);
    color: #fff;
    font-family: "Noto Serif JP", serif;
    font-weight: 700;
    font-size: 25px;
    display: flex;
    align-items: center;
    justify-content: center;
    letter-spacing: 1px;
  }
  .footer {
    position: absolute;
    left: 0; top: 1046px;
    width: 100%; height: 154px;
    display: flex;
    align-items: center;
    padding: 0 70px;
    box-sizing: border-box;
    gap: 40px;
  }
  .shop-mark {
    display: flex;
    align-items: center;
    gap: 12px;
    color: var(--red);
    font-weight: 900;
    font-size: 40px;
  }
  .shop-mark .square {
    width: 34px; height: 34px;
    background: var(--red);
  }
  .shop-info .name {
    font-weight: 900;
    font-size: 30px;
    line-height: 1.3;
  }
  .shop-info .name .branch { margin-left: 18px; }
  .shop-info .address,
  .shop-info .tel {
    font-size: 19px;
    line-height: 1.45;
  }
</style>
</head>
<body>
<div class="card">
  <div class="photo-top" role="img" aria-label="テーブルに置かれた老眼鏡のモノクロ写真"></div>
  <h1 class="headline" style="margin:0">最近、<br>老眼鏡の<br>度が合わない</h1>

  <div class="question-band">そう感じる機会、最近増えていませんか?</div>

  <div class="photo-bottom" role="img" aria-label="レンズ越しに見える眼鏡のモノクロ写真"></div>
  <div class="couple-photo" role="img" aria-label="笑顔のご年配のご夫婦の写真"></div>

  <p class="message" style="margin:0">老眼はどうしても年月が経つと共に少しずつ進行するため、2~3年に一度は「老眼鏡の見直し」が必要とされています。最近「老眼鏡が合わないな」とお感じの場合、ぜひ一度ご相談ください。</p>

  <div class="free-badge">
    <div class="service">眼鏡の調整<br>視力測定</div>
    <div class="free">無料</div>
    <div class="note">ご来店の際、お気軽に<br>お申し出下さい。</div>
  </div>

  <div class="welcome-band">スタッフ一同、ご来店を心よりお待ちしております</div>

  <footer class="footer">
    <div class="shop-mark"><span class="square"></span>ミエルド</div>
    <div class="shop-info">
      <div class="name">メガネのミエルド<span class="branch">東辻店</span></div>
      <div class="address">姫路市南辻町2丁目45-3</div>
      <div class="tel">TEL:079-000-4821</div>
    </div>
  </footer>
</div>
</body>
</html>
```